VERIDAX Need a luxury modern business card designed.

Need a luxury modern business card designed. refer to the uploaded files for the company name and logo in the zip file under source files. i will making my descion on monday. so please send in before then so if we need to edit we will have the time. we have a trade show coming up and im on a deadline for printer.

Target Market(s)

high end clients

Contact Information for Business Card

Company nAme and logo. Calvin Ostrow Co-Founder / Project Manager Office # 416-555-0193 Cell # 416-555-0147 VERIDAX.CA Calvin@veridax.ca

Font styles to use
Other font styles liked:
• Modern

Requirements
Must have
• Company name and logo, contact info, using the black, gold and white color scheme.

```html
<!DOCTYPE html>
<html lang="en">
<head>
<meta charset="utf-8">
<title>VERIDAX Business Card</title>
<link rel="stylesheet" href="https://fonts.googleapis.com/css2?family=Josefin+Sans:wght@300&family=Arimo:wght@400;700&display=swap">
<style>
  :root {
    --gold: #a89a65;
    --charcoal: #333333;
    --paper: #f8f8f9;
    --backdrop: #e4e4e4;
    --ink-light: #ffffff;
  }
  * { box-sizing: border-box; margin: 0; padding: 0; }
  html, body {
    width: 1200px;
    height: 900px;
    overflow: hidden;
    background: var(--backdrop);
  }
  .canvas {
    width: 1200px;
    height: 900px;
    display: flex;
    flex-direction: column;
    align-items: center;
    justify-content: center;
    gap: 48px;
  }
  .card {
    position: relative;
    width: 640px;
    height: 366px;
    overflow: hidden;
    box-shadow: 0 6px 18px rgba(0,0,0,0.12);
  }
  .card-front { background: var(--gold); }
  .wordmark {
    position: absolute;
    font-family: "Josefin Sans", sans-serif;
    font-weight: 300;
    letter-spacing: 0.14em;
    line-height: 1;
    white-space: nowrap;
  }
  .card-front .wordmark {
    left: 50%;
    top: 50%;
    transform: translate(-50%, -50%);
    font-size: 64px;
    color: var(--ink-light);
  }
  .card-back { background: var(--gold); }
  .card-back .shapes {
    position: absolute;
    inset: 0;
    width: 640px;
    height: 366px;
  }
  .card-back .wordmark {
    left: 505px;
    top: 128px;
    transform: translateX(-50%);
    font-size: 42px;
    color: var(--charcoal);
  }
  .identity {
    position: absolute;
    left: 54px;
    top: 51px;
    color: var(--ink-light);
    font-family: "Arimo", sans-serif;
    white-space: nowrap;
  }
  .identity .person-name {
    font-weight: 700;
    font-size: 22px;
    line-height: 1.05;
  }
  .identity .person-role {
    font-weight: 400;
    font-size: 14px;
    line-height: 1.25;
  }
  .contact-list {
    position: absolute;
    left: 196px;
    top: 238px;
    list-style: none;
    font-family: "Arimo", sans-serif;
    font-size: 13.5px;
    color: var(--ink-light);
    white-space: nowrap;
  }
  .contact-list li {
    display: flex;
    align-items: center;
    gap: 9px;
    height: 21px;
  }
  .contact-list svg {
    width: 14px;
    height: 14px;
    flex: none;
  }
</style>
</head>
<body>
<main class="canvas">

  <section class="card card-front" aria-label="Card front">
    <span class="wordmark">VERIDAX</span>
  </section>

  <section class="card card-back" aria-label="Card back">
    <svg class="shapes" viewBox="0 0 640 366" aria-hidden="true">
      <polygon points="300,0 640,0 640,366 412,366" fill="var(--paper)"/>
      <polygon points="0,44 314,44 332,102 0,102" fill="var(--charcoal)"/>
    </svg>

    <span class="wordmark">VERIDAX</span>

    <div class="identity">
      <p class="person-name">Calvin Ostrow</p>
      <p class="person-role">Co-Founder / Project Manager</p>
    </div>

    <ul class="contact-list">
      <li>
        <svg viewBox="0 0 16 16" aria-hidden="true"><path d="M4 2 L6.5 5 L5 6.5 C5.8 8.4 7.6 10.2 9.5 11 L11 9.5 L14 12 L12.3 14 C7 13.5 2.5 9 2 3.7 Z" fill="var(--ink-light)"/></svg>
        <span>416-555-0147</span>
      </li>
      <li>
        <svg viewBox="0 0 16 16" aria-hidden="true"><path d="M1 6 C1 3 15 3 15 6 L12 7 L11 5.5 L5 5.5 L4 7 Z" fill="var(--ink-light)"/><rect x="3" y="8" width="10" height="6" rx="1" fill="var(--ink-light)"/></svg>
        <span>416-555-0193</span>
      </li>
      <li>
        <svg viewBox="0 0 16 16" aria-hidden="true"><rect x="1.5" y="3.5" width="13" height="9" fill="none" stroke="var(--ink-light)"/><path d="M1.5 3.5 L8 9 L14.5 3.5" fill="none" stroke="var(--ink-light)"/></svg>
        <span>Calvin@veridax.ca</span>
      </li>
      <li>
        <svg viewBox="0 0 16 16" aria-hidden="true"><circle cx="8" cy="8" r="6.5" fill="none" stroke="var(--ink-light)"/><ellipse cx="8" cy="8" rx="3" ry="6.5" fill="none" stroke="var(--ink-light)"/><path d="M1.5 8 H14.5 M2.5 5 H13.5 M2.5 11 H13.5" stroke="var(--ink-light)" fill="none"/></svg>
        <span>VERIDAX.CA</span>
      </li>
    </ul>
  </section>

</main>
</body>
</html>
```